Stonelynk Business Card Design

The Stonelynk Co is an aggregate (crushing) equipment dealer serving Western Canadian provinces. Stonelynk is a distributor of aggregate equipment for different manufacturers.

We are looking to change and update the existing business card which has been used since the existence of the company. A copy of existing card has been attached for reference. The Stonelynk Co logo we want to remain the same and we want the green color to remain the same.

We are wanting something new with a different look. A refreshing card to show a new modern and updated look. No longer wanting to have the manufacturers on the back of the card but something more like our logo on the back of the card with a statement like "Crushing Solutions"

ideas could be:
- card can be different colors on front and back
- front or reverse of the card could possibly be the green color with the logo in black

Target Market(s)

Owners of Aggregate/Crushing companies

Requirements
Must have
• - logo to remain same along with same font within logo
• - green color to remain same
Nice to have
• as noted above under project description
Should not have

```html
<!DOCTYPE html>
<html lang="en">
<head>
<meta charset="utf-8">
<title>Stonelynk Co — Business Card</title>
<link rel="stylesheet" href="https://fonts.googleapis.com/css2?family=Roboto:wght@400;500;700;900&family=Roboto+Condensed:wght@400;500&display=swap">
<style>
  :root {
    --backdrop: #7b5339;
    --brand-green: #878a0a;
    --brand-green-text: #8a8c0c;
    --ink: #231f20;
    --card-white: #f4f4f2;
    --body-grey: #555555;
  }
  * { margin: 0; padding: 0; box-sizing: border-box; }
  html, body { width: 1200px; height: 960px; overflow: hidden; }
  body {
    background: var(--backdrop);
    position: relative;
    font-family: "Roboto", Arial, sans-serif;
  }
  .card {
    position: absolute;
    left: 320px;
    width: 600px;
    border-radius: 20px;
    box-shadow: 0 3px 8px rgba(0,0,0,0.35);
  }
  /* Front */
  .card-front {
    top: 105px;
    height: 345px;
    background: var(--brand-green);
    text-align: center;
  }
  .front-mark {
    position: absolute;
    left: 259px;
    top: 95px;
    width: 82px;
    height: 82px;
    border-radius: 50%;
    background: var(--ink);
  }
  .front-name {
    position: absolute;
    left: 0; right: 0;
    top: 220px;
    font-weight: 900;
    font-size: 24px;
    letter-spacing: 0.3px;
    color: var(--ink);
    padding-left: 10px;
  }
  .front-tagline {
    position: absolute;
    left: 0; right: 0;
    top: 294px;
    font-weight: 700;
    font-size: 14px;
    color: #2a2a18;
  }
  /* Back */
  .card-back {
    top: 493px;
    height: 342px;
    background: var(--card-white);
  }
  .back-brand {
    position: absolute;
    left: 330px;
    top: 36px;
    font-weight: 700;
    font-size: 13px;
    color: var(--brand-green-text);
    letter-spacing: 0.5px;
  }
  .person-name {
    position: absolute;
    left: 426px;
    top: 28px;
    font-family: "Roboto Condensed", "Arial Narrow", sans-serif;
    font-weight: 500;
    font-size: 22px;
    color: var(--brand-green-text);
    line-height: 1;
  }
  .person-title {
    position: absolute;
    left: 426px;
    top: 54px;
    font-family: "Roboto Condensed", "Arial Narrow", sans-serif;
    font-weight: 500;
    font-size: 15px;
    color: var(--ink);
    letter-spacing: 0.3px;
  }
  .address {
    position: absolute;
    left: 32px;
    top: 172px;
    font-size: 14px;
    line-height: 18px;
    color: var(--body-grey);
  }
  .contact-list {
    position: absolute;
    left: 32px;
    top: 218px;
    list-style: none;
    font-size: 14px;
    color: var(--body-grey);
  }
  .contact-list li {
    display: flex;
    align-items: center;
    height: 19.3px;
  }
  .contact-list svg {
    width: 14px;
    height: 14px;
    margin-right: 9px;
    fill: var(--brand-green-text);
  }
</style>
</head>
<body>
  <section class="card card-front">
    <div class="front-mark"></div>
    <div class="front-name">THE STONELYNK CO.</div>
    <div class="front-tagline">Crushing Solutions</div>
  </section>

  <section class="card card-back">
    <div class="back-brand">STONELYNK</div>
    <div class="person-name">DALE MORVEN</div>
    <div class="person-title">CEO/FOUNDER</div>

    <address class="address" style="font-style:normal">
      2210- 48B Avenue<br>
      Nisku, Alberta T9E 1K7
    </address>

    <ul class="contact-list">
      <li>
        <svg viewBox="0 0 16 16" aria-hidden="true"><path d="M3.5 1l2.5 3-1.5 1.8c.8 1.8 2.4 3.4 4.2 4.2L10.5 8.5l3 2.5-1.3 2.7C7 13.5 2.5 9 2.3 3.8z"/></svg>
        780.555.0142
      </li>
      <li>
        <svg viewBox="0 0 16 16" aria-hidden="true"><path d="M4.5 0.5h7a1 1 0 0 1 1 1v13a1 1 0 0 1-1 1h-7a1 1 0 0 1-1-1v-13a1 1 0 0 1 1-1zm.6 2v9.5h5.8V2.5zM8 12.8a.9.9 0 1 0 0 1.8.9.9 0 0 0 0-1.8z"/></svg>
        780.555.0187
      </li>
      <li>
        <svg viewBox="0 0 16 16" aria-hidden="true"><path d="M4 1h8v4H4zM1 6h14v6h-2.5v3h-9v-3H1zm4.5 4v3.5h5V10z"/></svg>
        780.555.0163
      </li>
      <li>
        <svg viewBox="0 0 16 16" aria-hidden="true"><path d="M1 3.5h14v9H1zm1.5 1.2v.4L8 9l5.5-3.9v-.4z"/></svg>
        dale@stonelynk.com
      </li>
      <li>
        <svg viewBox="0 0 16 16" aria-hidden="true"><path d="M8 1a7 7 0 1 0 0 14A7 7 0 0 0 8 1zm-2 3.2c1 .2 1.5 1 1.3 1.9-.3.9 1 1.2.7 2.3-.3 1-1.5.8-2 1.9-.3.8.2 2-.5 2.4A5.4 5.4 0 0 1 4.2 4.4zm4.6 8.4c-.2-1 .4-1.9 1.4-2.4.6-.3 1.1-1 1.4-1.6a5.4 5.4 0 0 1-2.8 4z"/></svg>
        www.stonelynk.ca
      </li>
    </ul>
  </section>
</body>
</html>
```